Best-selling author needs BOOK COVER DESIGN for "BRIGHT PUZZLES"

I need an impactful front and back cover design for my next non-fiction creative thinking book. Striking, modern, simple. Clean, with preference using black and red as dominant colours (but open to surprise).

Will be an e-book and printed book.
size; 6" x 9" (2:3 vertical rectangle)

barcode to come
some of the blurbs might change
insert author pic

Hope this is a great brief for you. Let me if any questions! ;)

Target Market(s)

Professionals. Maybe start-ups, entrepreneurs, or Fortune 500 execs

Industry/Entity Type

Business

Font styles to use
Serif
Sans Serif

Colors
f04a50
fece3e
fbee3e

Requirements
Must have
• FRONT COVER:
• title: BRIGHT PUZZLES
• subtitle: How to ask better questions to create breakthrough solutions.
• author name: Wren Tabor
• author descriptor: PANLx MC/Storyteller/Hothead
• review blurb: "The Perfect Storyteller!" - The Morning Ledger, UK.
• BACK COVER:
• title: Rock the New Economy with Explosive Questioning Skills.
• - Find out the Bright Puzzles that kick-started empires like NestLoop, Fenwick Dole, Brewhaven, Hydravolt, Sky Meridia, Lyrivo, Zintra, Orvello, Milo Grimsby, and, er, even FundSprout.
• - Learn how companies like T&W, Pomeral, Varnel, SkyTeal, Fablor, Larrowin, Valkor R9, Zumovi, and Dravelle use Bright Puzzles to develop blockbuster new products, experiences and marketing messages.
• - How to identify and eradicate your cognitive blindspots.
• - How to create a Curiosity Gap (and why that’s so important).
• - Why it’s important to challenge the Status Quo and how to do it.
• title: What if there was a formula for creating Bright Puzzles? There is!
• Get on board this rocket ship with business creativity expert (and best-selling author) Wren Tabor as he guides us through a proven system for creating more insightful, more powerful questions, which point us toward breakthrough solutions, products, and process innovations.
• For the first time, he shares the Bright Puzzle (Innovation Question Formulation) System here. The same system that he has taught to senior executives from major corporations such as Norvabank, Trekko, HoltmannVeyr, Korvath, Medvane, and many other progressive companies.
• title: Praise for Wren Tabor’s work:
• “Really impressive and inspiring. Causes us to really jump out of the box. The questioning and challenging skills we learned here really apply to our everyday R&D work situations.” Derek PuyanSo, Senior Innovation Engineer, HoltmannVeyr.
• “Blown away! This is really corruptive to everything I’ve been thinking. I recommend this because it is so original.” Brent Ho, trekko.
• "Wren Tabor is truly a subject matter expert." Martin Oyo, Norvabank.
• www.wrentabor,example
Nice to have
• Book contents is workbooky and workshopy in style (ie alot about getting stuff up on flipcharts) so some 'handwritten' Inkdash marker type like in some attached examples might be suitable.
• does it need a graphic element? up to you
Should not have
• Not too busy, not too fussy. Simple and strong. Boom!
• Don't use Question Mark in cliched way

```html
<!DOCTYPE html>
<html lang="en">
<head>
<meta charset="utf-8">
<title>Bright Puzzles – Cover Spread</title>
<link rel="stylesheet" href="https://fonts.googleapis.com/css2?family=Bebas+Neue&family=Arimo:wght@400;700&family=Montserrat:wght@600;700&family=Libre+Baskerville:ital@1&display=swap">
<style>
  :root {
    --page-bg: #f3f3f3;
    --cover-yellow: #ffe900;
    --accent-red: #f23548;
    --ink: #222222;
    --shadow-gold: #e9be1f;
    --paper: #ffffff;
  }
  * { margin: 0; padding: 0; box-sizing: border-box; }
  html, body { width: 1200px; height: 900px; overflow: hidden; }
  body {
    background: radial-gradient(ellipse at center, #ffffff 0%, var(--page-bg) 75%);
    position: relative;
    font-family: "Arimo", Arial, sans-serif;
    color: var(--ink);
  }
  .spread {
    position: absolute; left: 93px; top: 92px;
    width: 1013px; height: 713px;
    background: var(--cover-yellow);
    border: 1px solid #9a9a6a;
    overflow: hidden;
  }
  /* ---------- back cover ---------- */
  .back { position: absolute; left: 0; top: 0; width: 475px; height: 100%; }
  .back-title {
    position: absolute; left: 0; width: 475px; top: 40px;
    text-align: center; font-family: "Bebas Neue", sans-serif; font-weight: 400;
    color: var(--accent-red); font-size: 42px; line-height: 33px;
  }
  .back-heading {
    position: absolute; left: 25px; width: 430px; text-align: center;
    font-weight: 700; font-size: 12.5px; line-height: 17px;
  }
  .back-heading.rock { top: 122px; }
  .back-heading.formula { top: 287px; }
  .selling-points {
    position: absolute; left: 24px; top: 146px; width: 410px;
    list-style: none; font-size: 9.6px; line-height: 12.3px;
  }
  .selling-points li { margin-bottom: 5px; }
  .selling-points li::before { content: "• "; }
  .pitch {
    position: absolute; left: 24px; top: 330px; width: 408px;
    font-size: 9.6px; line-height: 12.3px; text-align: justify;
  }
  .pitch p { text-indent: 20px; margin-bottom: 13px; }
  .author-photo {
    position: absolute; left: 24px; top: 463px; width: 122px; height: 122px;
    border-radius: 50%; border: 2px solid var(--ink);
    background: radial-gradient(circle at 50% 40%, #d9d9d9, #6f6f6f);
  }
  .praise-title {
    position: absolute; left: 153px; top: 461px;
    font-weight: 700; font-size: 13px;
  }
  .praise { position: absolute; font-size: 9.6px; line-height: 12.3px; }
  .praise .quote { color: var(--accent-red); }
  .praise.one { left: 153px; top: 482px; width: 290px; }
  .praise.two { left: 153px; top: 544px; width: 290px; }
  .praise.three { left: 24px; top: 594px; width: 250px; }
  .barcode-space {
    position: absolute; left: 292px; top: 586px; width: 157px; height: 109px;
    background: var(--paper);
  }
  /* ---------- spine ---------- */
  .spine {
    position: absolute; left: 475px; top: 0; width: 63px; height: 100%;
    background: var(--accent-red);
    border-left: 2px dotted #b02030; border-right: 2px dotted #b02030;
  }
  .spine-text {
    position: absolute; left: 8px; top: 50px;
    writing-mode: vertical-rl; display: flex; align-items: center;
  }
  .spine-title {
    font-family: "Bebas Neue", sans-serif; font-size: 36px; color: var(--cover-yellow);
    line-height: 26px;
  }
  .spine-subtitle {
    font-family: "Montserrat", sans-serif; font-weight: 700; font-size: 10.5px;
    line-height: 12px; color: var(--cover-yellow); margin-top: 10px; margin-right: 4px;
  }
  .spine-subtitle .dark { color: var(--ink); }
  .spine-author {
    position: absolute; left: 20px; top: 518px; writing-mode: vertical-rl;
    font-family: "Montserrat", sans-serif; font-weight: 700; font-size: 17px;
    letter-spacing: 5px; color: var(--ink);
    border-top: 1px solid var(--ink); padding-top: 14px;
  }
  /* ---------- front cover ---------- */
  .front { position: absolute; left: 538px; top: 0; width: 475px; height: 100%; }
  .front-blurb {
    position: absolute; left: 0; width: 475px; top: 40px; text-align: center;
    font-family: "Libre Baskerville", serif; font-style: italic; font-size: 14.5px; line-height: 20px;
  }
  .front-title {
    position: absolute; left: 0; width: 475px; top: 96px; text-align: center;
    font-family: "Bebas Neue", sans-serif; font-weight: 400; color: var(--accent-red);
    font-size: 130px; line-height: 104px; letter-spacing: 3px;
  }
  .front-subtitle {
    position: absolute; left: 20px; width: 440px; top: 325px; text-align: center;
    font-family: "Montserrat", sans-serif; font-weight: 600; font-size: 16px;
    line-height: 20px; letter-spacing: 0.6px;
  }
  .front-subtitle .hot { color: var(--accent-red); }
  .subtitle-arrow { position: absolute; left: 404px; top: 324px; }
  .cover-graphic {
    position: absolute; left: 72px; top: 376px; width: 403px; height: 337px;
    background: linear-gradient(160deg, #222 0%, #2e2a1a 40%, var(--shadow-gold) 100%);
    opacity: 0.85;
  }
  .front-author {
    position: absolute; left: 0; width: 475px; top: 663px; text-align: center;
    font-family: "Montserrat", sans-serif; font-weight: 700; font-size: 22px; letter-spacing: 5px;
  }
</style>
</head>
<body>
  <main class="spread">
    <section class="back">
      <h2 class="back-title">BRIGHT<br>PUZZLES</h2>
      <h3 class="back-heading rock">Rock the New Economy with Explosive Questioning Skills.</h3>
      <ul class="selling-points">
        <li>Find out the Bright Puzzles that kick-started empires like NestLoop, Fenwick Dole, Brewhaven, Hydravolt, Sky Meridia, Lyrivo, Zintra, Orvello, Milo Grimsby, and, er, even FundSprout.</li>
        <li>Learn how companies like T&amp;W, Pomeral, Varnel, SkyTeal, Fablor, Larrowin, Valkor R9, Zumovi, and Dravelle use Bright Puzzles to develop blockbuster new products, experiences and marketing messages.</li>
        <li>How to identify and eradicate your cognitive blindspots.</li>
        <li>How to create a Curiosity Gap (and why that’s so important).</li>
        <li>Why it’s important to challenge the Status Quo and how to do it.</li>
      </ul>
      <h3 class="back-heading formula">What if there was a formula<br>for creating Bright Puzzles? There is!</h3>
      <div class="pitch">
        <p>Get on board this rocket ship with business creativity expert (and best-selling author) Wren Tabor as he guides us through a proven system for creating more insightful, more powerful questions, which point us toward breakthrough solutions, products, and process innovations.</p>
        <p>For the first time, he shares the Bright Puzzle (Innovation Question Formulation) System here. The same system that he has taught to senior executives from major corporations such as Norvabank, Trekko, HoltmannVeyr, Korvath, Medvane, and many other progressive companies.</p>
      </div>
      <div class="author-photo" role="img" aria-label="Portrait of author Wren Tabor"></div>
      <h3 class="praise-title">Praise for Wren Tabor’s work:</h3>
      <div class="praise one">
        <p class="quote">“Really impressive and inspiring. Causes us to really jump out of the box. The questioning and challenging skills we learned here really apply to our everyday R&amp;D work situations.”</p>
        <p>- Derek PuyanSo, Senior Innovation Engineer, HoltmannVeyr</p>
      </div>
      <div class="praise two">
        <p class="quote">“Blown away! This is really corruptive to everything I’ve been thinking. I recommend this because it is so original.”</p>
        <p>- Brent Ho, Trekko</p>
      </div>
      <div class="praise three">
        <p class="quote">“Wren Tabor is truly a subject matter expert.”</p>
        <p>- Martin Oyo, Norvabank</p>
      </div>
      <div class="barcode-space"></div>
    </section>

    <section class="spine">
      <div class="spine-text">
        <span class="spine-title">BRIGHT PUZZLES</span>
        <span class="spine-subtitle"><span class="dark">HOW TO ASK</span> BETTER QUESTIONS<br><span class="dark">TO CREATE</span> BREAKTHROUGH SOLUTIONS</span>
      </div>
      <div class="spine-author">WREN TABOR</div>
    </section>

    <section class="front">
      <p class="front-blurb">"The Perfect Storyteller!"<br>- The Morning Ledger, UK</p>
      <h1 class="front-title">BRIGHT<br>PUZZLES</h1>
      <p class="front-subtitle">HOW TO ASK <span class="hot">BETTER QUESTIONS</span><br>TO CREATE <span class="hot">BREAKTHROUGH SOLUTIONS</span></p>
      <svg class="subtitle-arrow" width="40" height="28" viewBox="0 0 40 28">
        <path d="M3 9 C14 0 32 1 30 18" fill="none" stroke="#222" stroke-width="2.5"/>
        <path d="M24 14 L30 21 L36 13" fill="none" stroke="#222" stroke-width="2.5"/>
      </svg>
      <div class="cover-graphic" role="img" aria-label="Graphic of black stairs rising to an open door, with a red blocky question mark and a long golden shadow"></div>
      <p class="front-author">WREN TABOR</p>
    </section>
  </main>
</body>
</html>
```